Hotel Newsletter Design

We need 4 newsletter templates for a luxurious hotel. The templates only differ in the headers (basically each has different images based on a certain theme and/or distinguishing colours). Please feel free to use other colour that those on the webpage of the hotel.

Previous newsletters were these:

"Wine bar" - http://www.marbleoakinn.example/newsletter.php?id=76&lang=en
"Feast" - http://www.marbleoakinn.example/newsletter.php?id=75&lang=en
"Hotel" - http://www.marbleoakinn.example/newsletter.php?id=77&lang=en
"Restaurant" - http://www.marbleoakinn.example/newsletter.php?id=78&lang=en

These were too basic and old-fashioned, we need something more UP-TO-DATE, FRESH, MORE MODERN DESIGN.

The final newsletter will be an HTML page with an editable section.

So upon designing please pay attention to leave a space for editable content, which is going to be text and images.

Header and footer required, these won't be editable.

The 4 different header themes are Wine bar, Hotel, Feast, Restaurant.

the website of the hotel:
http://www.marbleoakinn.example/
images that can be used:
http://www.vextrapod.example/temp/bemo/images.zip

Target Market(s)

Luxurious Hotel Visitors

Industry/Entity Type

Hospitality

Requirements
Must have
• Logo in the header, address and contact in the footer
Nice to have
• Modern design
Should not have
• Old fashioned design

```html
<!DOCTYPE html>
<html lang="en">
<head>
<meta charset="utf-8">
<title>Marble Oak Inn – Newsletter</title>
<link rel="stylesheet" href="https://fonts.googleapis.com/css2?family=Mulish:wght@700;800&family=Arimo:ital,wght@0,400;0,700;1,700&display=swap">
<style>
  :root{
    --page-bg:#2a1810;
    --page-bg-deep:#1a0e08;
    --panel-top:#5a4a44;
    --panel-bottom:#1f1714;
    --panel-line:#8a7a74;
    --rule:#7d6e68;
    --text:#ffffff;
    --text-soft:#e6d6cf;
    --link:#2fb3e8;
    --brand-red:#b3262b;
    --banner-red:#cc0000;
    --banner-green:#6f8a10;
    --banner-text:#ecdcdc;
    --footer-bg:#000000;
    --placeholder-grey:#a9a9a9;
  }
  *{box-sizing:border-box;margin:0;padding:0}
  html,body{width:725px;height:1200px;overflow:hidden}
  body{
    position:relative;
    background:radial-gradient(ellipse at 80% 70%,#3a2114 0%,var(--page-bg) 45%,var(--page-bg-deep) 100%);
    font-family:"Arimo",Arial,sans-serif;
    color:var(--text);
  }
  .header-photo{
    position:absolute;left:0;top:0;width:725px;height:305px;
    background:
      radial-gradient(circle at 90px 75px,#fff6c0 0,#e6c04a 40px,transparent 110px),
      radial-gradient(circle at 668px 150px,#fff3b0 0,#d8b040 35px,transparent 100px),
      linear-gradient(180deg,#6a4a12 0%,#8c6a22 35%,#5a3c12 70%,#2e1c08 100%);
  }
  .published{
    position:absolute;left:82px;top:0;width:561px;height:25px;
    background:rgba(40,30,10,.55);
    font-size:12px;font-weight:700;text-align:right;padding:5px 22px 0 0;
  }
  .published span{margin-left:16px;font-weight:400}
  .brand-band{
    position:absolute;left:82px;top:167px;width:561px;height:120px;
    background:rgba(120,120,120,.45);
  }
  .brand-name{
    position:absolute;left:130px;top:262px;
    font-family:"Arimo",Arial,sans-serif;font-size:16px;font-weight:400;
    color:var(--brand-red);letter-spacing:.5px;
  }
  .brand-mark{
    position:absolute;left:165px;top:200px;width:44px;height:44px;border-radius:50%;
    background:var(--brand-red);
  }
  .header-thumb{
    position:absolute;left:378px;top:183px;width:216px;height:104px;
    border:6px solid #e9e9e9;
    background:linear-gradient(180deg,#6a4812 0%,#b48a3a 45%,#d8c6a8 75%,#8a6a40 100%);
  }
  .panel{
    position:absolute;left:82px;top:305px;width:561px;height:850px;
    background:linear-gradient(180deg,var(--panel-top) 0%,#3a2c28 40%,var(--panel-bottom) 100%);
    border:1px solid var(--panel-line);border-top:none;
  }
  .main-col{position:absolute;left:107px;top:334px;width:290px}
  .section-title{font-family:"Mulish",sans-serif;font-weight:800;font-size:18.5px;line-height:22px}
  .lead{margin-top:11px;font-size:12.4px;line-height:15.6px;font-weight:700;font-style:italic;color:var(--text-soft)}
  .body-copy{margin-top:13px;font-size:12.4px;line-height:15.6px;font-weight:700}
  .body-copy a{color:var(--link);text-decoration:none}
  .rule{position:absolute;left:105px;width:290px;height:1px;background:var(--rule)}
  .article-image{
    position:absolute;left:107px;top:647px;width:210px;height:134px;
    border:1px solid #d8d8d8;
    background:linear-gradient(180deg,#999 0%,var(--placeholder-grey) 60%,#b5b5b5 100%);
  }
  .article{position:absolute;left:107px;top:798px;width:285px}
  .article-title{font-family:"Mulish",sans-serif;font-weight:800;font-size:17.5px;line-height:22px}
  .article .body-copy{margin-top:12px;line-height:15.3px}
  .content-slot{
    position:absolute;left:108px;top:965px;width:286px;height:52px;
    background:linear-gradient(180deg,#888 0%,#6e6e6e 100%);
  }
  .column-divider{position:absolute;left:416px;top:340px;width:2px;height:712px;background:#6e625d}
  .side-heading{
    position:absolute;left:435px;width:201px;height:25px;
    background:linear-gradient(180deg,#3a3331 0%,#141111 100%);
    border:1px solid #6a605c;
    font-size:12px;font-weight:700;padding:5px 0 0 17px;letter-spacing:.2px;
  }
  .news{position:absolute;left:437px;top:376px;width:192px;font-size:9.4px;line-height:12.2px;font-weight:700}
  .news p+p{margin-top:12px}
  .news a{color:var(--link);text-decoration:none}
  .banner{
    position:absolute;left:439px;width:187px;height:188px;
    border:1px solid #8a7a74;
    display:flex;align-items:center;justify-content:center;
    font-size:17px;font-weight:700;color:var(--banner-text);
  }
  .banner--red{top:617px;background:var(--banner-red)}
  .banner--green{top:838px;background:var(--banner-green)}
  .footer{
    position:absolute;left:82px;top:1068px;width:561px;height:87px;
    background:var(--footer-bg);border:1px solid var(--panel-line);border-top:none;
  }
  .legal{position:absolute;left:17px;top:15px;width:360px;font-size:7.6px;line-height:13px}
  .unsubscribe{position:absolute;left:20px;top:55px;font-size:7.6px}
  .address{position:absolute;right:16px;top:8px;text-align:right;font-size:9.4px;line-height:14px}
</style>
</head>
<body>
  <div class="header-photo" role="img" aria-label="Warm lamplit hotel bedroom with a double bed under a sloped ceiling"></div>
  <div class="published">Published <span>June 3, 2010</span></div>
  <div class="brand-band"></div>
  <div class="brand-mark"></div>
  <div class="brand-name">Marble Oak Inn</div>
  <div class="header-thumb" role="img" aria-label="Twin hotel room with two beds and bedside lamps"></div>

  <div class="panel"></div>

  <section class="main-col">
    <h1 class="section-title">Content Areas</h1>
    <p class="lead">Consequat vel illum: dolore eu feugiat nulla facilisis at vero eros et. Laoreet dolore magna aliquam erat; volutpat ut wisi enim ad minim veniam quis nostrud.</p>
    <p class="body-copy">Nisl ut aliquip ex ea commodo consequat duis autem vel eum iriure dolor in hendrerit. Elit sed diam nonummy nibh euismod tincidunt ut laoreet dolore magna aliquam erat. Nulla facilisis at vero eros, et accumsan et? Delenit augue duis nihil imperdiet doming id quod mazim? Consuetudium lectorum mirum, est notare quam littera gothica quam nunc. Ipsum dolor sit amet consectetuer adipiscing elit sed. Erat volutpat ut wisi enim ad minim veniam quis nostrud exerci tation ullamcorper <a href="#">suscipit lobortis</a>.</p>
  </section>
  <div class="rule" style="top:623px"></div>
  <div class="article-image"></div>
  <article class="article">
    <h2 class="article-title">Lorem Zuli Ipselum<br>mazim est quod</h2>
    <p class="body-copy">Consuetudium lectorum mirum, est notare quam littera gothica quam nunc. Ipsum dolor sit amet consectetuer adipiscing elit sed. Erat volutpat ut wisi enim ad minim veniam quis nostrud exerci tation ullamcorper suscipit lobortis.</p>
  </article>
  <div class="rule" style="top:952px"></div>
  <div class="content-slot"></div>

  <div class="column-divider"></div>

  <div class="side-heading" style="top:338px">RECENT NEWS / EVENTS</div>
  <div class="news">
    <p>Eros et accumsan et</p>
    <p>Iusto odio dignissim qui blandit praesent luptatum zzril delenit augue duis. Facer possim <a href="#">assum typi</a> non habent claritatem insitam est usus legentis. Minim veniam quis nostrud exerci tation ullamcorper suscipit lobortis nisl ut aliquip ex ea commodo!</p>
    <p>&nbsp;Esse molestie consequat vel illum dolore eu, feugiat nulla facilisis at vero dolore! Consuetudium lectorum mirum est, notare quam littera gothica. Id quod mazim placerat in iis qui facit eorum.</p>
  </div>
  <div class="side-heading" style="top:574px">LATEST PROMOTIONS</div>
  <div class="banner banner--red">BANNER</div>
  <div class="banner banner--green">BANNER</div>

  <footer class="footer">
    <p class="legal">Legal text Legal textLegal textLegal textLegal textLegal textLegal textLegal textLegal textLegal textLegal textLegal textLegal textLegal textLegal textLegal textLegal text</p>
    <p class="unsubscribe">UNSUBSCRIBE TEXT HERE</p>
    <address class="address" style="font-style:normal">Marble Oak Inn Hotel<br>Address 1<br>Address 2<br>+phone number<br>website</address>
  </footer>
</body>
</html>
```